New Business Card for General Contractor Marketing

Need a business card the is more like a marketing promotion of our services
Must be horizontal orientation, One Sided Only, Max font size, Organize the Services
#1 General Contractor for Realtors
Remodels – Renovations – Repairs
Water & Mold Damage Experts
Painting: Interior/ Exterior
Flooring: Wood / LVT / Carpet
Plumbing: Repairs & Upgrades
Electric: Lights & Energy Efficient Upgrades
Kitchen & Bath Remodels
Fast Inspections Repair Billed Thru Escrow
BrightHarborBuilds.com
555-418-2796

Industry/Entity Type

General Contractor

Contact Information for Business Card

One Sided Only: #1 General Contractor for Realtors Remodels – Renovations – Repairs Water & Mold Damage Experts Painting: Interior/ Exterior Flooring: Wood / LVT / Carpet Plumbing: Repairs & Upgrades Electric: Lights & Energy Efficient Upgrades Kitchen & Bath Remodels Fast Inspections Repair Billed Thru Escrow BrightHarborBuilds.com 555-418-2796

Colors
0054AA
0677BA
7BADD7
CADEEF
E8F1F8

Requirements
Must have
• One Sided Only: #1 General Contractor for Realtors Remodels – Renovations – Repairs Water & Mold Damage Experts Painting: Interior/ Exterior Flooring: Wood / LVT / Carpet Plumbing: Repairs & Upgrades Electric: Lights & Energy Efficient Upgrades Kitchen & Bath Remodels Fast Inspections Repair Billed Thru Escrow BrightHarborBuilds.com 555-418-2796

```html
<!DOCTYPE html>
<html lang="en">
<head>
<meta charset="utf-8">
<title>General Contractor for Realtors – Business Card</title>
<link href="https://fonts.googleapis.com/css2?family=Roboto+Condensed:wght@500;700&family=Orbitron:wght@700&family=Arimo:wght@400&display=swap" rel="stylesheet">
<style>
  :root {
    --page-bg: #e8f1f8;
    --card-white: #ffffff;
    --brand-blue: #0054aa;
    --mid-blue: #0677ba;
    --sky-blue: #7badd7;
    --pale-blue: #cadeef;
    --ice-blue: #e8f1f8;
  }
  * { box-sizing: border-box; margin: 0; padding: 0; }
  html, body {
    width: 1200px; height: 1200px; overflow: hidden;
    background: var(--page-bg);
  }
  .card {
    position: absolute; left: 75px; top: 300px;
    width: 1050px; height: 600px;
    border-radius: 40px; overflow: hidden;
    background: var(--card-white);
    font-family: "Roboto Condensed", "Arial Narrow", sans-serif;
  }
  .card-identity {
    position: absolute; left: 0; top: 0; width: 470px; height: 100%;
    background: var(--card-white); text-align: center; color: var(--brand-blue);
  }
  .brand {
    position: absolute; left: 0; top: 62px; width: 100%;
    display: flex; justify-content: center; align-items: center; gap: 12px;
  }
  .brand-square { width: 26px; height: 26px; background: var(--mid-blue); }
  .brand-name { font-weight: 700; font-size: 40px; line-height: 1; color: var(--brand-blue); }
  .headline {
    position: absolute; left: 0; top: 148px; width: 100%;
    font-weight: 700; font-size: 46px; line-height: 50px; color: var(--brand-blue);
  }
  .tagline {
    position: absolute; left: 0; top: 266px; width: 100%;
    font-weight: 700; font-size: 22px; line-height: 1; color: var(--mid-blue);
  }
  .divider {
    position: absolute; left: 60px; top: 330px; width: 350px; height: 3px;
    background: var(--pale-blue);
  }
  .escrow-note {
    position: absolute; left: 0; top: 366px; width: 100%;
    font-weight: 500; font-size: 22px; line-height: 1; color: var(--brand-blue);
  }
  .call-line {
    position: absolute; left: 0; top: 420px; width: 100%;
    font-family: "Orbitron", sans-serif; font-weight: 700;
    font-size: 30px; line-height: 1; color: var(--mid-blue); letter-spacing: 1px;
  }
  .website {
    position: absolute; left: 0; top: 476px; width: 100%;
    font-family: "Arimo", Arial, sans-serif; font-size: 22px; line-height: 1;
    letter-spacing: 0.5px; color: var(--brand-blue);
  }
  .card-services {
    position: absolute; left: 470px; top: 0; width: 580px; height: 100%;
    background: var(--brand-blue); text-align: center; color: var(--ice-blue);
  }
  .services-title {
    position: absolute; left: 0; top: 62px; width: 100%;
    font-weight: 700; font-size: 33px; letter-spacing: 13px;
    padding-left: 13px; line-height: 1; color: var(--pale-blue);
  }
  .services-list {
    position: absolute; left: 0; top: 128px; width: 100%;
    list-style: none; font-weight: 700; font-size: 34px; line-height: 50px;
  }
  .services-list .bullet { color: var(--sky-blue); font-size: 24px; vertical-align: 4px; margin-right: 8px; }
</style>
</head>
<body>
  <article class="card">
    <header class="card-identity">
      <div class="brand">
        <span class="brand-square"></span>
        <span class="brand-name">Bright Harbor Builds</span>
      </div>
      <h1 class="headline">General Contractor<br>for Realtors</h1>
      <p class="tagline">Remodels – Renovations – Repairs</p>
      <div class="divider"></div>
      <p class="escrow-note">Fast Inspections Repair Billed Thru Escrow</p>
      <p class="call-line">CALL&nbsp; 555-418-2796</p>
      <p class="website">BrightHarborBuilds.com</p>
    </header>
    <section class="card-services">
      <h2 class="services-title">SERVICES</h2>
      <ul class="services-list">
        <li><span class="bullet">•</span>Water &amp; Mold Damage Experts</li>
        <li><span class="bullet">•</span>Painting: Interior/ Exterior</li>
        <li><span class="bullet">•</span>Flooring: Wood / LVT / Carpet</li>
        <li><span class="bullet">•</span>Plumbing: Repairs &amp; Upgrades</li>
        <li><span class="bullet">•</span>Electric: Lights &amp;</li>
        <li>Energy Efficient Upgrades</li>
        <li><span class="bullet">•</span>Kitchen &amp; Bath Remodels</li>
      </ul>
    </section>
  </article>
</body>
</html>
```